New company that wants to specialize in presale property and garden do ups

I own A landscaping and premium garden maintenance company.
I want to advertise to people that are listing there homes for sale.
For the purpose of using my company services to fix up there home and gardens to maximize there sale potential. I am on instagram as tvmeadow_landscaping. I am aiming for the higher end of the market. This Flyer will be post card size. I would like my logo to be used. And your layout to be clean cut and easy to read. I need my clients to understand that spending time on there gardens appearance will aid with sale of there home and maximize there profit
Target Market(s)
People selling there homes. or thinking about selling there homes
Industry/Entity Type
Landscape Gardening
Requirements
Must have
- Email address doug@tvmeadow.example.nz number 0271234567 and the instagram logo
- The benefits of spending money of the look and feel of gardens to maximize there chance of quick and profitable sale. wow factor and so on. Free estimate no obligation
Nice to have
- Any thing you can add to the layout that would help as sound professional and get our point across.

```html
<!DOCTYPE html>
<html lang="en">
<head>
<meta charset="utf-8">
<title>TV Meadow Landscaping – Postcard</title>
<link href="https://fonts.googleapis.com/css2?family=Bebas+Neue&family=Roboto+Condensed:wght@700&family=Lato:wght@400&display=swap" rel="stylesheet">
<style>
  :root {
    --blue: #0a52a0;
    --green: #9bc93c;
    --grey-band: #7c7c7c;
    --ink: #1c1c1c;
    --panel: #e9e9e9;
    --white: #ffffff;
  }
  * { margin: 0; padding: 0; box-sizing: border-box; }
  html, body { width: 1200px; height: 912px; overflow: hidden; background: var(--white); }
  .postcard {
    position: absolute; left: 0; top: 56px;
    width: 1200px; height: 800px; overflow: hidden; background: var(--white);
  }
  .postcard-art { position: absolute; inset: 0; }
  .headline { position: absolute; left: 35px; top: 50px; }
  .headline-top {
    font-family: "Bebas Neue", sans-serif; color: var(--blue);
    font-size: 94px; line-height: 84px; letter-spacing: -1px;
  }
  .headline-main {
    font-family: "Roboto Condensed", sans-serif; font-weight: 700; color: var(--green);
    font-size: 110px; line-height: 96px; letter-spacing: 2px;
  }
  .service-band {
    position: absolute; left: 31px; top: 270px;
    font-family: "Roboto Condensed", sans-serif; font-weight: 700; color: var(--white);
    font-size: 41px; line-height: 48px; letter-spacing: 0.5px;
  }
  .benefit {
    position: absolute; left: 32px; top: 413px;
    font-family: "Lato", sans-serif; color: var(--ink); font-size: 18px; line-height: 22px;
  }
  .call {
    position: absolute; left: 32px; top: 490px;
    font-family: "Roboto Condensed", sans-serif; font-weight: 700; font-size: 58px; line-height: 64px;
  }
  .call-label { color: var(--blue); margin-right: 6px; }
  .call-number { color: var(--ink); }
  .social { position: absolute; left: 34px; top: 690px; display: flex; gap: 20px; }
  .social-mark { width: 33px; height: 33px; border: 3px solid var(--white); border-radius: 6px; }
  .email {
    position: absolute; left: 33px; top: 738px;
    font-family: "Lato", sans-serif; color: var(--ink); font-size: 24px;
  }
  .estimate-panel {
    position: absolute; left: 822px; top: 548px; width: 318px;
    text-align: center; font-family: "Roboto Condensed", sans-serif; font-weight: 700;
  }
  .brand-name {
    color: var(--ink); font-size: 28px; line-height: 32px; letter-spacing: 1px;
    text-transform: uppercase; margin-bottom: 64px;
  }
  .estimate-line { font-size: 30px; line-height: 34px; }
  .estimate-line.free { color: var(--blue); }
  .estimate-line.obligation { color: var(--ink); }
</style>
</head>
<body>
<main class="postcard">
  <svg class="postcard-art" width="1200" height="800" viewBox="0 0 1200 800">
    <defs>
      <linearGradient id="gardenTone" x1="0" y1="0" x2="0.3" y2="1">
        <stop offset="0" stop-color="#5f8f3a"/>
        <stop offset="0.45" stop-color="#8fb660"/>
        <stop offset="0.75" stop-color="#cf5a6a"/>
        <stop offset="1" stop-color="#e3b0c9"/>
      </linearGradient>
      <linearGradient id="turfTone" x1="0" y1="0" x2="0" y2="1">
        <stop offset="0" stop-color="#5e8f35"/>
        <stop offset="0.45" stop-color="#7da24a"/>
        <stop offset="0.6" stop-color="#4a3e33"/>
        <stop offset="1" stop-color="#3a322b"/>
      </linearGradient>
    </defs>

    <!-- grey service band -->
    <rect class="service-band-bg" x="0" y="264" width="600" height="118" fill="var(--grey-band)"/>

    <!-- garden photo area -->
    <path role="img" aria-label="Photo: children watering spring flowers in a garden"
          d="M588 0 Q534 284 732 448 L870 525 Q1020 560 1200 480 L1200 0 Z" fill="url(#gardenTone)"/>
    <path d="M548 0 Q490 300 712 460" fill="none" stroke="var(--white)" stroke-width="30"/>
    <path d="M556 0 Q500 296 716 452" fill="none" stroke="var(--blue)" stroke-width="8"/>
    <path d="M582 0 Q528 284 728 448" fill="none" stroke="var(--green)" stroke-width="10"/>
    <path d="M860 540 Q1030 575 1200 490" fill="none" stroke="var(--green)" stroke-width="10"/>
    <path d="M860 556 Q1030 592 1200 506" fill="none" stroke="var(--blue)" stroke-width="6"/>

    <!-- round turf photo -->
    <circle cx="666" cy="494" r="134" fill="var(--blue)"/>
    <circle cx="666" cy="494" r="128" fill="var(--white)"/>
    <circle cx="666" cy="494" r="124" fill="var(--green)"/>
    <circle role="img" aria-label="Photo: hands laying a strip of fresh turf on soil"
            cx="666" cy="494" r="118" fill="url(#turfTone)"/>

    <!-- estimate panel -->
    <path d="M822 500 Q822 488 834 488 L1128 488 Q1140 488 1140 500 L1140 800 L822 800 Z" fill="var(--panel)"/>

    <!-- bottom wave -->
    <path d="M0 626 C250 566 520 640 760 722 C950 786 1090 770 1200 684 L1200 800 L0 800 Z" fill="var(--white)"/>
    <path d="M0 626 C250 566 520 640 760 722 C950 786 1090 770 1200 684 L1200 700 C1090 790 950 804 760 740 C520 660 250 594 0 660 Z" fill="var(--blue)"/>
    <path d="M0 670 C250 606 520 672 760 752 C950 814 1090 800 1200 718 L1200 800 L0 800 Z" fill="var(--green)"/>
    <path d="M820 772 C960 806 1090 794 1200 718" fill="none" stroke="var(--white)" stroke-width="4"/>
  </svg>

  <h1 class="headline">
    <div class="headline-top">IF ITS OUTDOORS</div>
    <div class="headline-main">WE DO IT!</div>
  </h1>

  <p class="service-band">complete landscaping and<br>garden maintenance service</p>

  <p class="benefit">The benefits of spending money of the look and feel of gardens<br>to maximize there chance of quick and profitable sale</p>

  <p class="call"><span class="call-label">Call:</span><span class="call-number">0271234567</span></p>

  <div class="social" aria-label="Social media">
    <span class="social-mark"></span>
    <span class="social-mark"></span>
  </div>
  <p class="email">doug@tvmeadow.example.nz</p>

  <div class="estimate-panel">
    <p class="brand-name">TV Meadow<br>Landscaping</p>
    <p class="estimate-line free">FREE ESTIMATE</p>
    <p class="estimate-line obligation">NO OBLIGATION</p>
  </div>
</main>
</body>
</html>
```